Business Card Design

colour scheme is to be grey background and light green writing
i would like some kind of brick arch highlighted in green and the writing inside the arch in green also
on the back list..all types of brickwork, no job to small, free quote and space to write a small quote underneath

Industry/Entity Type

Business

Contact Information for Business Card

RQT Brickwork
0481536207
morvikteal48@quillbox.net

```html
<!DOCTYPE html>
<html lang="en">
<head>
<meta charset="utf-8">
<title>RQT Brickwork – Business Card</title>
<link rel="stylesheet" href="https://fonts.googleapis.com/css2?family=Orbitron:wght@700&family=Open+Sans:wght@300&display=swap">
<style>
  :root {
    --stage: #f1f1f1;
    --card-grey: #414244;
    --card-grey-light: #505154;
    --card-grey-dark: #343537;
    --lime: #a6d62a;
    --white: #ffffff;
  }
  * { box-sizing: border-box; margin: 0; padding: 0; }
  html, body {
    width: 1200px;
    height: 800px;
    overflow: hidden;
    background: var(--stage);
  }
  .stage {
    position: relative;
    width: 1200px;
    height: 800px;
  }
  .card {
    position: absolute;
    top: 245px;
    width: 540px;
    height: 310px;
    border-radius: 20px;
    box-shadow: 0 6px 18px rgba(0, 0, 0, 0.25);
    overflow: hidden;
  }
  .card--front {
    left: 40px;
    background: radial-gradient(ellipse at 35% 45%, var(--card-grey-light), var(--card-grey-dark) 85%);
  }
  .card--back {
    left: 620px;
    background: var(--card-grey);
  }

  /* Front */
  .front__brand {
    position: absolute;
    left: 0;
    top: 0;
    width: 250px;
    height: 100%;
    display: flex;
    align-items: center;
    justify-content: center;
  }
  .brand-name {
    font-family: "Orbitron", sans-serif;
    font-weight: 700;
    color: var(--lime);
    letter-spacing: 0.06em;
    text-align: center;
    line-height: 1.25;
  }
  .front__brand .brand-name { font-size: 24px; }
  .front__divider {
    position: absolute;
    left: 250px;
    top: 40px;
    width: 1px;
    height: 230px;
    background: var(--lime);
  }
  .front__details {
    position: absolute;
    left: 282px;
    top: 0;
    height: 100%;
    display: flex;
    flex-direction: column;
    justify-content: center;
    gap: 10px;
  }
  .person-name {
    font-family: "Orbitron", sans-serif;
    font-weight: 700;
    font-size: 30px;
    color: var(--lime);
    letter-spacing: 0.05em;
    margin-bottom: 6px;
  }
  .contact-line {
    display: flex;
    align-items: center;
    gap: 8px;
    font-family: "Open Sans", sans-serif;
    font-weight: 300;
    font-size: 16px;
    color: var(--lime);
  }
  .contact-line svg { width: 14px; height: 14px; flex: none; }

  /* Back */
  .card--back {
    display: flex;
    align-items: center;
    justify-content: center;
  }
  .back__brand { font-size: 38px; }
</style>
</head>
<body>
<main class="stage">

  <section class="card card--front" aria-label="Card front">
    <div class="front__brand">
      <p class="brand-name">RQT<br>Brickwork</p>
    </div>
    <div class="front__divider"></div>
    <div class="front__details">
      <h1 class="person-name">Your Name</h1>
      <p class="contact-line">
        <svg viewBox="0 0 14 14" aria-hidden="true">
          <rect x="3" y="0.5" width="8" height="13" rx="1.5" fill="var(--lime)"/>
          <rect x="4.5" y="2.5" width="5" height="7" fill="var(--card-grey-dark)"/>
          <circle cx="7" cy="11.5" r="0.9" fill="var(--card-grey-dark)"/>
        </svg>
        <span>0481536207</span>
      </p>
      <p class="contact-line">
        <svg viewBox="0 0 14 14" aria-hidden="true">
          <rect x="0.5" y="2.5" width="13" height="9" fill="var(--lime)"/>
          <polyline points="0.5,2.5 7,8 13.5,2.5" fill="none" stroke="var(--card-grey-dark)" stroke-width="1.2"/>
        </svg>
        <span>morvikteal48@quillbox.net</span>
      </p>
    </div>
  </section>

  <section class="card card--back" aria-label="Card back">
    <p class="brand-name back__brand">RQT Brickwork</p>
  </section>

</main>
</body>
</html>
```